Lionel Arbusto and Dwight Halvorsen Advertisement

We would like an ad that conveys understated elegance. We are a company that purchases estate jewelry watches and diamonds. We care to a wealthy, upscale clientele.

Target Market(s)

Wealthy upscale.

Industry/Entity Type

It Company

Requirements
Must have
• Elegant Design. Crisp Clean. Attached a doc of how the ad should be arranged.

```html
<!DOCTYPE html>
<html lang="en">
<head>
<meta charset="utf-8">
<title>Lionel Arbusto &amp; Dwight Halvorsen — Ready To Sell</title>
<link href="https://fonts.googleapis.com/css2?family=Cantarell:wght@700&family=Marcellus+SC&family=Cinzel:wght@700&family=Open+Sans:wght@400&display=swap" rel="stylesheet">
<style>
  :root {
    --ink: #111111;
    --ink-soft: #333333;
    --paper: #ffffff;
    --mist: #eeeeee;
    --mist-deep: #d9d9d9;
    --band-dark: #4a4a4a;
    --band-grey: #b5b5b5;
  }
  * { margin: 0; padding: 0; box-sizing: border-box; }
  html, body { width: 1000px; height: 1200px; overflow: hidden; background: var(--paper); }
  .ad {
    position: relative;
    width: 1000px;
    height: 1200px;
    overflow: hidden;
    background: radial-gradient(ellipse 70% 50% at 50% 35%, var(--mist) 0%, #f6f6f6 55%, var(--paper) 100%);
    color: var(--ink);
    text-align: center;
  }
  .headline {
    position: absolute; top: 48px; left: 0; right: 0;
    font-family: "Cantarell", "Helvetica Neue", sans-serif;
    font-weight: 700; font-size: 92px; letter-spacing: 1px;
  }
  .hero-stone {
    position: absolute; left: 320px; top: 180px; width: 370px; height: 360px;
    border-radius: 18px;
    background: radial-gradient(circle at 45% 40%, #ffffff 0%, #e4e4e4 45%, #bdbdbd 80%, #dcdcdc 100%);
    transform: rotate(-10deg);
  }
  .brand-mark {
    position: absolute; left: 478px; top: 600px; width: 44px; height: 44px;
    border: 2px solid var(--ink-soft);
  }
  .brand-name {
    position: absolute; top: 690px; left: 0; right: 0;
    font-family: "Marcellus SC", "Times New Roman", serif;
    font-size: 33px; color: var(--ink-soft);
  }
  .tagline {
    position: absolute; top: 738px; left: 0; right: 0;
    display: flex; align-items: center; justify-content: center; gap: 12px;
    font-family: "Marcellus SC", serif; font-size: 15px; letter-spacing: 1px; color: var(--ink-soft);
  }
  .tagline::before, .tagline::after { content: ""; width: 230px; height: 1px; background: var(--ink-soft); }
  .promise {
    position: absolute; top: 782px; left: 0; right: 0;
    font-family: "Marcellus SC", serif; font-size: 62px; color: var(--ink);
  }
  .booking {
    position: absolute; top: 862px; left: 0; right: 0;
    font-family: "Cinzel", serif; font-weight: 700; font-size: 40px;
  }
  .swoosh { position: absolute; left: 0; top: 800px; width: 1000px; height: 400px; }
  .contact {
    position: absolute; left: 0; right: 0;
    font-family: "Open Sans", Arial, sans-serif; font-size: 24px; color: var(--ink-soft);
    display: flex; align-items: center; justify-content: center; gap: 8px;
  }
  .contact svg { width: 20px; height: 20px; }
  .contact--venue { top: 938px; }
  .contact--street { top: 970px; }
  .contact--email { top: 1013px; font-size: 22px; }
</style>
</head>
<body>
<main class="ad">
  <svg class="swoosh" viewBox="0 0 1000 400" aria-hidden="true">
    <defs>
      <linearGradient id="greyBand" x1="0" y1="0" x2="0" y2="1">
        <stop offset="0" stop-color="#e8e8e8"/>
        <stop offset="1" stop-color="#a9a9a9"/>
      </linearGradient>
      <linearGradient id="lightWedge" x1="0" y1="0" x2="1" y2="0">
        <stop offset="0" stop-color="#ffffff" stop-opacity="0"/>
        <stop offset="1" stop-color="#cfcfcf"/>
      </linearGradient>
    </defs>
    <path d="M300,255 C600,230 850,160 1000,95 L1000,145 C720,245 420,280 120,275 Z" fill="url(#lightWedge)"/>
    <path d="M0,268 C320,320 700,255 1000,145 L1000,200 C700,300 350,330 0,282 Z" fill="var(--band-dark)"/>
    <path d="M0,300 C350,350 720,305 1000,220 L1000,400 L0,400 Z" fill="url(#greyBand)"/>
  </svg>

  <h1 class="headline">Ready To SELL?</h1>
  <div class="hero-stone" role="img" aria-label="Photograph of a large emerald-cut diamond"></div>

  <div class="brand-mark" aria-hidden="true"></div>
  <p class="brand-name">Lionel Arbusto &amp; Dwight Halvorsen</p>
  <p class="tagline">Your Best Option</p>

  <p class="promise">Utmost Discretion</p>
  <p class="booking">By Appointment</p>

  <p class="contact contact--venue">Via Solenne</p>
  <p class="contact contact--street">
    <svg viewBox="0 0 20 20" aria-hidden="true"><path d="M10 2a5 5 0 0 0-5 5c0 4 5 9 5 9s5-5 5-9a5 5 0 0 0-5-5zm0 7a2 2 0 1 1 0-4 2 2 0 0 1 0 4z" fill="none" stroke="#333" stroke-width="1.6"/><path d="M5 18h10" stroke="#333" stroke-width="1.6"/></svg>
    118-B Larkspur Avenue, Coral Mesa, FL 33999
  </p>
  <p class="contact contact--email">
    <svg viewBox="0 0 20 20" aria-hidden="true"><rect x="2" y="5" width="16" height="11" fill="none" stroke="#333" stroke-width="1.4"/><path d="M2 5l8 6 8-6" fill="none" stroke="#333" stroke-width="1.4"/></svg>
    contact@arbustohalvorsen.com
  </p>
</main>
</body>
</html>
```